Yard Sign Design for Roofing Contractor

We are looking for a new design for our yard signs used on all jobs we build. We are looking for a way to brand the company and are hoping that this contest can give us a "theme" we can incorporate into out other marketing items such as, vehicle graphics, apparel, etc... I have attached a copy of our logo to be used on the sign, it can be "shadowed" with a color to enhance the look and the sign, but please keep the basic logo design. Attached are some samples of construction colors the boss was thinking of along with a picture of our current yard sign to help give some direction and let you know what info is needed on the sign.The darker construction yellow may work better than the fluorescent yellow, but won't know without visual aid. We are not tied to any particular color as of now, so they do have freedom of design as long as keeping with the construction feel. (Just another thought, potentially a reflective construction tape look would be interesting so signs are visable at night)
Updates

Reason: Meeting with new web designers next week to discuss best option to incorporate into our website.Thank you for the submissions!

Target Market(s)

Want signs to stand out when driving by and visibility in neighborhood where sign is posted for potential referrals

Industry/Entity Type

Contractor

Colors
fbed22
fece3e
f37122

Requirements
Must have
• Information that is on our current signs, image attached. I uploaded a .pdf file showing some options that could work for adding "shading" to our logo if you choose to do so.
• Sign should measure 18" T, 24" W
Nice to have
• Interested is seeing designs using construction tape look, images attached

```html
<!DOCTYPE html>
<html lang="en">
<head>
<meta charset="utf-8">
<title>Halvern Construction Yard Sign</title>
<link href="https://fonts.googleapis.com/css2?family=Montserrat:wght@600;700&display=swap" rel="stylesheet">
<style>
  :root {
    --page: #e9e9e6;
    --sign-black: #0c0c0c;
    --construction-yellow: #fbed22;
    --logo-yellow: #fece3e;
    --safety-orange: #f37122;
    --white: #ffffff;
  }
  html, body {
    margin: 0;
    padding: 0;
    overflow: hidden;
  }
  .canvas {
    width: 1200px;
    height: 1000px;
    background: var(--page);
    position: relative;
    overflow: hidden;
  }
  .yard-sign {
    position: absolute;
    left: 80px;
    top: 110px;
    width: 1040px;
    height: 780px;
    background: var(--sign-black);
    overflow: hidden;
    box-shadow: 0 6px 24px rgba(0,0,0,0.18);
  }
  .tape {
    position: absolute;
    left: 0;
    width: 100%;
  }
  .tape--top { top: 0; height: 95px; }
  .tape--bottom { bottom: 0; height: 170px; }
  .award-seal {
    position: absolute;
    left: 45px;
    top: 120px;
    width: 180px;
    height: 180px;
    border-radius: 50%;
    background: var(--logo-yellow);
    border: 14px solid var(--safety-orange);
    box-sizing: border-box;
    display: flex;
    align-items: center;
    justify-content: center;
    text-align: center;
    font-family: "Montserrat", sans-serif;
    font-weight: 700;
    font-size: 26px;
    line-height: 1.2;
    color: var(--sign-black);
    transform: rotate(-12deg);
  }
  .listing-badge {
    position: absolute;
    left: 905px;
    top: 128px;
    width: 80px;
    height: 170px;
    background: var(--white);
    border-radius: 8px;
  }
  .company-name {
    position: absolute;
    left: 240px;
    top: 200px;
    width: 650px;
    text-align: center;
    font-family: "Montserrat", sans-serif;
    font-weight: 700;
    font-size: 70px;
    color: var(--logo-yellow);
    line-height: 1.15;
    margin: 0;
  }
  .company-name span { display: block; }
  .services {
    position: absolute;
    left: 250px;
    top: 440px;
    width: 560px;
    display: flex;
    justify-content: space-between;
    font-family: "Montserrat", sans-serif;
    font-weight: 700;
    font-size: 30px;
    letter-spacing: 1px;
    text-transform: uppercase;
    color: var(--logo-yellow);
    margin: 0;
    padding: 0;
    list-style: none;
  }
  .phone {
    position: absolute;
    left: 0;
    top: 505px;
    width: 100%;
    text-align: center;
    font-family: "Montserrat", sans-serif;
    font-weight: 700;
    font-size: 92px;
    color: var(--safety-orange);
    margin: 0;
    line-height: 1;
  }
  .website {
    position: absolute;
    left: 0;
    top: 610px;
    width: 100%;
    text-align: center;
    font-family: "Montserrat", sans-serif;
    font-weight: 600;
    font-size: 40px;
    color: var(--white);
    margin: 0;
    line-height: 1;
  }
</style>
</head>
<body>
<main class="canvas">
  <section class="yard-sign">
    <svg class="tape tape--top" viewBox="0 0 1040 95" preserveAspectRatio="none" role="img" aria-label="Construction hazard tape band">
      <rect x="0" y="0" width="1040" height="35" fill="var(--construction-yellow)"/>
      <rect x="0" y="45" width="1040" height="50" fill="var(--construction-yellow)"/>
    </svg>

    <div class="award-seal">Award<br>Winning</div>
    <div class="listing-badge" aria-hidden="true"></div>

    <h1 class="company-name">
      <span>HALVERN</span>
      <span>CONSTRUCTION</span>
    </h1>

    <ul class="services">
      <li>Roof</li>
      <li>Siding</li>
      <li>Gutters</li>
    </ul>

    <p class="phone">555-214-0190</p>
    <p class="website">www.halvernroofing.com</p>

    <svg class="tape tape--bottom" viewBox="0 0 1040 170" preserveAspectRatio="none" role="img" aria-label="Construction hazard tape band">
      <polygon points="0,110 1040,40 1040,60 0,130" fill="var(--construction-yellow)"/>
      <polygon points="0,138 1040,68 1040,170 0,170" fill="var(--construction-yellow)"/>
    </svg>
  </section>
</main>
</body>
</html>
```